Silver Brook Custom Homes business card. Double sided. Modern. professional

Silver Brook Custom Homes
contemporary modern design with our logo /
Double sided with all our contact information
Use same Green colors as in our Logo. Contemporary logo that grabs your attention. Visually pleasing and balanced. Easy to read, and Vibrant. Would love an option for rounded edges. Embossed logo would be amazing.
Contact Information for Business Card
Dana Pellman Owner / General Contractor Silver Brook Custom Homes p: 555.201.0142 m: 555.318.0178 e: silverbrookcustomhomes@mailnest.example w: www.silverbrookcustomhomes.example 218 Wrenfield Mill Road Fernhollow, ZZ 29088

```html
<!DOCTYPE html>
<html lang="en">
<head>
<meta charset="utf-8">
<title>Silver Brook Custom Homes – Business Card</title>
<link href="https://fonts.googleapis.com/css2?family=Cinzel:wght@500;600&family=Montserrat:wght@400;500&display=swap" rel="stylesheet">
<style>
  :root {
    --backdrop: #d6d6d6;
    --card-front: #ffffff;
    --card-back: #18191b;
    --green: #5f7f2c;
    --green-light: #6f8f33;
    --ink: #1f1f1f;
  }
  * { margin: 0; padding: 0; box-sizing: border-box; }
  html, body { width: 1200px; height: 965px; overflow: hidden; }
  body {
    background: var(--backdrop);
    position: relative;
    font-family: "Montserrat", sans-serif;
    color: var(--ink);
  }
  .card {
    position: absolute;
    top: 159px;
    width: 383px;
    height: 669px;
    border-radius: 26px;
  }
  .card-front { left: 186px; background: var(--card-front); }
  .card-back  { left: 653px; background: var(--card-back); }

  .brand {
    position: absolute;
    left: 0; right: 0;
    text-align: center;
  }
  .brand-mark {
    display: block;
    margin: 0 auto 16px;
    width: 150px; height: 150px;
    border-radius: 50%;
    background: var(--green-light);
  }
  .brand-name {
    font-family: "Cinzel", serif;
    font-weight: 500;
    font-size: 35px;
    line-height: 1;
    letter-spacing: 1px;
    color: var(--green);
    white-space: nowrap;
  }
  .brand-sub {
    margin-top: 4px;
    font-size: 10px;
    font-weight: 500;
    line-height: 1;
    letter-spacing: 8px;
    padding-left: 8px;
    color: var(--green);
    text-transform: uppercase;
  }
  .card-front .brand { top: 33px; }
  .card-back .brand { top: 230px; }

  .person {
    position: absolute;
    top: 340px; left: 0; right: 0;
    text-align: center;
  }
  .person-name {
    font-family: "Cinzel", serif;
    font-weight: 600;
    font-size: 31px;
    color: var(--green);
    line-height: 1;
  }
  .person-title {
    margin-top: 6px;
    font-size: 16px;
  }

  .icon-row {
    position: absolute;
    top: 430px; left: 27px; right: 27px;
    height: 22px;
    display: flex;
    align-items: center;
    gap: 8px;
  }
  .icon-row .rule {
    flex: 1;
    height: 2px;
    background: var(--green);
  }
  .icon-row .rule-left { background: linear-gradient(to right, transparent, var(--green) 40%); margin-right: 6px; }
  .icon-row .rule-right { background: linear-gradient(to left, transparent, var(--green) 40%); margin-left: 6px; }
  .icon {
    width: 22px; height: 22px;
    background: var(--green);
    display: flex; align-items: center; justify-content: center;
  }
  .icon svg { width: 14px; height: 14px; }

  .contact {
    position: absolute;
    top: 472px; left: 0; right: 0;
    text-align: center;
    font-size: 15px;
    line-height: 21px;
  }
  .contact .accent { color: var(--green); }
  .contact .email { font-size: 14px; }

  .divider {
    position: absolute;
    top: 576px; left: 27px; right: 27px;
    height: 2px;
    background: var(--green);
  }
  .address {
    position: absolute;
    top: 597px; left: 0; right: 0;
    text-align: center;
    font-size: 16px;
    line-height: 22px;
  }
</style>
</head>
<body>
  <section class="card card-front">
    <div class="brand">
      <span class="brand-mark"></span>
      <div class="brand-name">SILVER BROOK</div>
      <div class="brand-sub">Custom Homes</div>
    </div>

    <div class="person">
      <div class="person-name">Dana Pellman</div>
      <div class="person-title">Owner / General Contractor</div>
    </div>

    <div class="icon-row">
      <span class="rule rule-left"></span>
      <span class="icon" aria-label="phone">
        <svg viewBox="0 0 24 24"><path fill="#fff" d="M6.6 10.8a15 15 0 0 0 6.6 6.6l2.2-2.2c.3-.3.7-.4 1-.2 1.1.4 2.3.6 3.6.6.6 0 1 .4 1 1V20c0 .6-.4 1-1 1A17 17 0 0 1 3 4c0-.6.4-1 1-1h3.5c.6 0 1 .4 1 1 0 1.3.2 2.5.6 3.6.1.3 0 .7-.2 1z"/></svg>
      </span>
      <span class="icon" aria-label="mobile">
        <svg viewBox="0 0 24 24"><rect x="6" y="2" width="12" height="20" rx="2" fill="none" stroke="#fff" stroke-width="2"/><circle cx="12" cy="18" r="1.2" fill="#fff"/></svg>
      </span>
      <span class="icon" aria-label="email">
        <svg viewBox="0 0 24 24"><rect x="3" y="5" width="18" height="14" rx="1" fill="none" stroke="#fff" stroke-width="2"/><path d="M3 6l9 7 9-7" fill="none" stroke="#fff" stroke-width="2"/></svg>
      </span>
      <span class="icon" aria-label="website">
        <svg viewBox="0 0 24 24" fill="none" stroke="#fff" stroke-width="1.6"><circle cx="12" cy="12" r="9"/><ellipse cx="12" cy="12" rx="4" ry="9"/><path d="M3 12h18M4.5 7.5h15M4.5 16.5h15"/></svg>
      </span>
      <span class="rule rule-right"></span>
    </div>

    <div class="contact">
      <div>555.201.0142</div>
      <div>555.318.0178</div>
      <div class="email">silverbrookcustomhomes@mailnest.example</div>
      <div>www.<span class="accent">silverbrookcustomhomes</span>.example</div>
    </div>

    <div class="divider"></div>

    <div class="address">
      <div>218 Wrenfield Mill Road</div>
      <div>Fernhollow, ZZ 29088</div>
    </div>
  </section>

  <section class="card card-back">
    <div class="brand">
      <span class="brand-mark"></span>
      <div class="brand-name">SILVER BROOK</div>
      <div class="brand-sub">Custom Homes</div>
    </div>
  </section>
</body>
</html>
```